LLC needs a business card design that emphasizes consulting and expert witness in upstream oil and g

I need a business card design for my company called Kelvora Consultative Service, LLC. My expertise is in oil and gas upstream operations management to optimize performance and also as an expert witness for law firms in oil and gas upstream operations litigation.
The final design should communicate knowledge and hands-on experience as well as trust. (Kelvora means rope or lasso. Perhaps "Kelvora" should be in the form of a rope.) I do not like the color green in any shade. My first preference would be some shade of blue.
Oil And Gas

```html
<!DOCTYPE html>
<html lang="en">
<head>
<meta charset="utf-8">
<title>Kelvora Consultative Service, LLC – Business Card</title>
<link rel="stylesheet" href="https://fonts.googleapis.com/css2?family=Open+Sans:wght@400;600;800&display=swap">
<style>
  :root {
    --bg: #f3f3f3;
    --card: #ffffff;
    --blue: #0a6aa6;
    --blue-deep: #0a5e9c;
    --blue-light: #0b8ebf;
    --orange: #ec7a2e;
    --gray-text: #4a4a4a;
    --font: "Open Sans", Arial, sans-serif;
  }
  * { box-sizing: border-box; margin: 0; padding: 0; }
  html, body { width: 1200px; height: 1000px; overflow: hidden; }
  body {
    background: var(--bg);
    font-family: var(--font);
    position: relative;
  }
  .card {
    position: absolute;
    overflow: hidden;
    box-shadow: 0 2px 10px rgba(0,0,0,0.12);
  }
  .card-art { position: absolute; inset: 0; width: 100%; height: 100%; }

  /* Front (portrait) */
  .card--front {
    left: 88px; top: 160px; width: 368px; height: 645px;
    background: var(--card);
  }
  .brand { position: absolute; left: 0; right: 0; text-align: center; }
  .card--front .brand { top: 62px; }
  .brand-name {
    font-weight: 800;
    font-size: 58px;
    letter-spacing: 3px;
    line-height: 1;
    color: var(--blue);
  }
  .brand-tagline {
    margin-top: 14px;
    font-weight: 400;
    font-size: 18px;
    letter-spacing: 1.2px;
    color: var(--blue);
  }
  .person { position: absolute; top: 243px; left: 0; right: 0; text-align: center; }
  .person-name { font-size: 17px; font-weight: 600; color: var(--blue); }
  .person-title { margin-top: 6px; font-size: 15px; color: var(--gray-text); letter-spacing: 0.3px; }

  .contacts { position: absolute; top: 388px; left: 86px; list-style: none; }
  .contacts li { display: flex; height: 26.5px; align-items: center; font-size: 15px; color: var(--gray-text); letter-spacing: 0.3px; }
  .contact-key { width: 31px; font-weight: 800; color: var(--blue); }

  /* Back (landscape) */
  .card--back {
    left: 490px; top: 395px; width: 645px; height: 368px;
    background: var(--blue);
  }
  .card--back .brand { top: 140px; left: 150px; right: 0; }
  .card--back .brand-name { color: #ffffff; font-size: 62px; }
  .card--back .brand-tagline { color: #ffffff; }
</style>
</head>
<body>

  <section class="card card--front" aria-label="Business card front">
    <svg class="card-art" viewBox="0 0 368 645" aria-hidden="true">
      <defs>
        <radialGradient id="frontBlue" cx="0.55" cy="0.95" r="0.7">
          <stop offset="0" stop-color="#0b92c2"/>
          <stop offset="1" stop-color="#0a5e9c"/>
        </radialGradient>
      </defs>
      <path class="swoosh-orange" fill="var(--orange)"
            d="M0,380 C12,480 80,560 187,567 C110,562 40,550 0,535 Z"/>
      <path class="band-blue" fill="url(#frontBlue)"
            d="M0,545 C70,572 150,580 215,578 C300,572 350,510 368,430 L368,645 L0,645 Z"/>
    </svg>

    <div class="brand">
      <div class="brand-name">KELVORA</div>
      <div class="brand-tagline">CONSULTATIVE SERVICE, LLC</div>
    </div>

    <div class="person">
      <div class="person-name">Daniel Hartwell</div>
      <div class="person-title">Director &amp; Operations Manager</div>
    </div>

    <ul class="contacts">
      <li><span class="contact-key">O</span>555.210.4821</li>
      <li><span class="contact-key">M</span>555.318.7046</li>
      <li><span class="contact-key">E</span>daniel@kelvora.com</li>
      <li><span class="contact-key">W</span>www.kelvora.com</li>
    </ul>
  </section>

  <section class="card card--back" aria-label="Business card back">
    <svg class="card-art" viewBox="0 0 645 368" aria-hidden="true">
      <defs>
        <radialGradient id="backBlue" cx="0.5" cy="0.05" r="0.9">
          <stop offset="0" stop-color="#0b8ebf"/>
          <stop offset="1" stop-color="#0a5e9c"/>
        </radialGradient>
      </defs>
      <rect width="645" height="368" fill="url(#backBlue)"/>
      <path class="swoosh-orange" fill="var(--orange)"
            d="M0,110 C25,240 110,330 220,368 L172,368 C92,330 22,250 0,150 Z"/>
      <path class="corner-white" fill="#ffffff"
            d="M0,150 C22,250 92,330 172,368 L0,368 Z"/>
    </svg>

    <div class="brand">
      <div class="brand-name">KELVORA</div>
      <div class="brand-tagline">CONSULTATIVE SERVICE, LLC</div>
    </div>
  </section>

</body>
</html>
```